Business Card Design Project

We are an agricultural business based in Brisbane.
We design, manage and operate regional saleyards. Our logo is green/silver in colour and details of our business can be found on our website www.vodemarketyards.com.au

Just wanting a corporate design for some business cards and include name, position, contact details.

Thanks

Industry/Entity Type

Business

```html
<!DOCTYPE html>
<html lang="en">
<head>
<meta charset="utf-8">
<title>Vode Market Yards – Business Card</title>
<link rel="stylesheet" href="https://fonts.googleapis.com/css2?family=Roboto+Slab:wght@800&family=Arimo:wght@400;700&display=swap">
<style>
  :root {
    --page-bg: #e9e9e6;
    --card-white: #f7f8f8;
    --brand-green: #0f8a3c;
    --brand-green-dark: #0b5e2a;
    --brand-green-deep: #074a20;
    --ink: #1d1d1d;
    --on-green: #ffffff;
  }
  * { margin: 0; padding: 0; box-sizing: border-box; }
  html, body { width: 1200px; height: 880px; overflow: hidden; background: var(--page-bg); }
  .canvas {
    width: 1200px; height: 880px;
    display: flex; flex-direction: column; align-items: center; justify-content: center; gap: 40px;
  }
  .card {
    position: relative; width: 640px; height: 391px; overflow: hidden;
    box-shadow: 0 6px 18px rgba(0,0,0,0.18);
  }

  /* Front */
  .card-front { background: var(--card-white); }
  .wordmark {
    position: absolute; text-align: center;
    font-family: "Roboto Slab", Georgia, serif; font-weight: 800;
    letter-spacing: 1px; line-height: 1.02; text-transform: uppercase;
  }
  .card-front .wordmark { left: 170px; top: 70px; width: 420px; font-size: 46px; color: var(--ink); }
  .holder { position: absolute; left: 40px; top: 196px; font-family: "Arimo", Arial, sans-serif; }
  .holder-name { font-weight: 700; font-size: 24px; color: var(--brand-green); }
  .holder-role { font-size: 19px; color: var(--ink); margin-top: 4px; }
  .divider { position: absolute; left: 310px; top: 246px; width: 2px; height: 92px; background: var(--brand-green); }
  .contacts { position: absolute; left: 328px; top: 248px; list-style: none; font-family: "Arimo", Arial, sans-serif; font-size: 16px; color: var(--ink); }
  .contacts li { display: flex; align-items: center; gap: 10px; height: 30px; white-space: nowrap; }
  .contacts svg { width: 17px; height: 17px; flex: none; }
  .edge-line { position: absolute; left: 0; right: 0; bottom: 14px; height: 3px; background: var(--brand-green); }
  .edge-band { position: absolute; left: 311px; right: 0; bottom: 0; height: 14px; background: var(--brand-green); }

  /* Back */
  .card-back { background: var(--brand-green-dark); }
  .yard-photo {
    position: absolute; inset: 0;
    background: linear-gradient(135deg, var(--brand-green) 0%, var(--brand-green-dark) 55%, var(--brand-green-deep) 100%);
  }
  .card-back .wordmark { left: 0; right: 0; top: 128px; font-size: 56px; color: var(--on-green); }
</style>
</head>
<body>
<main class="canvas">
  <section class="card card-front" aria-label="Business card front">
    <div class="wordmark">Vode Market<br>Yards</div>
    <div class="holder">
      <p class="holder-name">Dale Morrow</p>
      <p class="holder-role">Managing Director</p>
    </div>
    <div class="divider"></div>
    <ul class="contacts">
      <li>
        <svg viewBox="0 0 18 18" aria-hidden="true"><rect x="3" y="1" width="12" height="16" rx="2" fill="#1d1d1d"/><rect x="5" y="3" width="8" height="10" fill="#f7f8f8"/><circle cx="9" cy="15" r="1" fill="#f7f8f8"/></svg>
        <span>+00 123 456 789</span>
      </li>
      <li>
        <svg viewBox="0 0 18 18" aria-hidden="true"><rect x="1" y="4" width="16" height="11" rx="1" fill="#1d1d1d"/><path d="M1.5 4.5 L9 10 L16.5 4.5" fill="none" stroke="#f7f8f8" stroke-width="1.4"/></svg>
        <span>dale@vodemarketyards.com.au</span>
      </li>
      <li>
        <svg viewBox="0 0 18 18" aria-hidden="true"><circle cx="9" cy="9" r="8" fill="#1d1d1d"/><g fill="none" stroke="#f7f8f8" stroke-width="1"><ellipse cx="9" cy="9" rx="3.5" ry="8"/><line x1="1" y1="9" x2="17" y2="9"/><line x1="9" y1="1" x2="9" y2="17"/></g></svg>
        <span>www.vodemarketyards.com.au</span>
      </li>
    </ul>
    <div class="edge-line"></div>
    <div class="edge-band"></div>
  </section>

  <section class="card card-back" aria-label="Business card back">
    <div class="yard-photo" role="img" aria-label="Green-toned photograph of cattle in saleyard pens"></div>
    <div class="wordmark">Vode Market<br>Yards</div>
  </section>
</main>
</body>
</html>
```